Business Card design for sports marketing creative agency

We need a business card designed for a sports marketing agency.
Side 1: Vosk | 720
Gold Vosk 720 brand
Division of Vosk | a creative agency that focuses on athletes
Modern look
Info on Card:
vosk720.com
@vosk_720
Peter R. Lund
Director of Client Services
M: 555.287.4193
E. peter@vosk720.com
Side 2:
Red Vosk | a creative agency brand
Marketing Creative Agency
Modern look
Info on card:
Vosk | a creative agency (red logo)
voskstudio.com
@voskstudio
Target Market(s)
Pro athletes
Industry/Entity Type
Marketing
Look and feel
Each slider illustrates characteristics of the customer's brand and the style your logo design should communicate.

```html
<!DOCTYPE html>
<html lang="en">
<head>
<meta charset="utf-8">
<title>Vosk business cards</title>
<link href="https://fonts.googleapis.com/css2?family=Source+Sans+3:wght@400;600;700&family=Didact+Gothic&display=swap" rel="stylesheet">
<style>
  :root {
    --page: #ffffff;
    --card: #ffffff;
    --gold: #a8823a;
    --gold-light: #c9a453;
    --gold-faint: #efe6d8;
    --red: #d0172b;
    --red-deep: #b3122a;
    --red-faint: #f5e2dc;
    --white: #ffffff;
  }
  * { margin: 0; padding: 0; box-sizing: border-box; }
  html, body {
    width: 1200px; height: 1200px; overflow: hidden;
    background: var(--page);
    font-family: "Source Sans 3", "Myriad Pro", Arial, sans-serif;
  }
  .canvas { position: relative; width: 1200px; height: 1200px; }
  .card {
    position: absolute; left: 160px; width: 862px; height: 435px;
    background: var(--card);
    box-shadow: 6px 8px 10px rgba(0,0,0,0.55), 0 0 3px rgba(0,0,0,0.08);
  }
  .card--gold { top: 98px; }
  .card--red { top: 593px; }
  .card > * { position: absolute; }

  .brand-name, .watermark-name {
    font-family: "Source Sans 3", Arial, sans-serif;
    font-weight: 600; line-height: 1; white-space: nowrap;
  }
  .brand-divider, .watermark-divider { width: 2px; }
  .brand-tag, .watermark-tag {
    font-family: "Didact Gothic", "Century Gothic", sans-serif;
    line-height: 1; white-space: nowrap;
  }

  /* gold card */
  .card--gold .brand-name { left: 30px; top: 68px; font-size: 130px; color: var(--gold); }
  .card--gold .brand-divider { left: 331px; top: 70px; height: 114px; background: var(--gold); }
  .card--gold .brand-tag { left: 350px; top: 95px; font-size: 52px; color: var(--gold); }
  .card--gold .notes { left: 30px; top: 216px; font-size: 13px; line-height: 17px; color: var(--gold); }
  .card--gold .name-band {
    left: 410px; top: 229px; width: 452px; height: 54px;
    background: linear-gradient(90deg, var(--gold) 0%, var(--gold-light) 55%, #f6efe0 70%, var(--gold-light) 78%, var(--gold) 100%);
  }
  .card--gold .watermark { left: 32px; top: 322px; }
  .card--gold .watermark-name { font-size: 80px; color: var(--gold-faint); }
  .card--gold .watermark-divider { height: 62px; background: var(--gold-faint); }
  .card--gold .watermark-tag { font-size: 30px; color: var(--gold-faint); }
  .card--gold .contact { left: 567px; top: 322px; font-size: 15px; color: var(--gold); }

  .watermark { display: flex; align-items: center; gap: 10px; }

  .name-band { color: var(--white); font-weight: 700; font-size: 18px; line-height: 25px; padding: 2px 0 0 48px; }

  .contact { display: flex; flex-direction: column; gap: 6px; }
  .contact-row { display: flex; align-items: center; gap: 6px; height: 18px; }
  .contact-row svg { width: 14px; height: 14px; flex: none; }
  .contact-row--web { margin-top: 6px; font-size: 13px; }

  /* red card */
  .card--red .brand-name { left: 26px; top: 67px; font-size: 118px; color: var(--red); }
  .card--red .brand-divider { left: 302px; top: 67px; height: 106px; background: var(--red); }
  .card--red .brand-tag { left: 320px; top: 104px; font-size: 48px; color: var(--red); }
  .card--red .notes { left: 26px; top: 211px; font-size: 17px; line-height: 23px; color: var(--red-deep); }
  .card--red .name-band {
    left: 410px; top: 230px; width: 452px; height: 52px;
    background: linear-gradient(90deg, #e61c2a 0%, #e31b2b 60%, var(--red-deep) 100%);
  }
  .card--red .watermark { left: 28px; top: 330px; }
  .card--red .watermark-name { font-size: 70px; color: var(--red-faint); }
  .card--red .watermark-divider { height: 60px; background: var(--red-faint); }
  .card--red .watermark-tag { font-size: 27px; color: var(--red-faint); }
  .card--red .contact { left: 576px; top: 364px; font-size: 14px; color: var(--red-deep); gap: 2px; }
  .card--red .contact-row--social { padding-left: 84px; font-size: 15px; }
</style>
</head>
<body>
<main class="canvas">

  <section class="card card--gold" aria-label="Vosk 720 business card">
    <div class="brand-name">Vosk</div>
    <div class="brand-divider"></div>
    <div class="brand-tag">720</div>
    <div class="notes">
      <p>Vosk | 720</p>
      <p>Gold Vosk 720 brand</p>
      <p>Division of Vosk | a creative agency that focuses on athletes</p>
      <p>Modern look</p>
    </div>
    <div class="name-band">
      <p>Peter R. Lund</p>
      <p>Director of Client Services</p>
    </div>
    <div class="watermark" aria-hidden="true">
      <div class="watermark-name">Vosk</div>
      <div class="watermark-divider"></div>
      <div class="watermark-tag">720</div>
    </div>
    <div class="contact">
      <div class="contact-row">
        <svg viewBox="0 0 16 16"><path fill="currentColor" d="M1 6c0-2 3-3 7-3s7 1 7 3v1h-3V5.5H4V7H1z M4 8h8l2 5H2z"/></svg>
        <span>: 555.287.4193</span>
      </div>
      <div class="contact-row">
        <svg viewBox="0 0 16 16"><rect x="1.5" y="4" width="13" height="9" fill="none" stroke="currentColor" stroke-width="1.4"/><path d="M1.5 4l6.5 5 6.5-5" fill="none" stroke="currentColor" stroke-width="1.4"/></svg>
        <span>. peter@vosk720.com</span>
      </div>
      <div class="contact-row contact-row--web">
        <svg viewBox="0 0 16 16"><circle cx="8" cy="8" r="7" fill="currentColor"/><path d="M4 5c2 0 3 1 2 3s1 3 0 5M10 3c-1 2 1 3 3 3" fill="none" stroke="#fff" stroke-width="1.2"/></svg>
        <span>http//www.vosk720.com</span>
      </div>
    </div>
  </section>

  <section class="card card--red" aria-label="Vosk creative agency business card">
    <div class="brand-name">Vosk</div>
    <div class="brand-divider"></div>
    <div class="brand-tag">a creative agency</div>
    <div class="notes">
      <p>Red Vosk | a creative agency brand</p>
      <p>Marketing Creative Agency</p>
      <p>Modern look</p>
    </div>
    <div class="name-band">
      <p>Peter R. Lund</p>
      <p>Director of Client Services</p>
    </div>
    <div class="watermark" aria-hidden="true">
      <div class="watermark-name">Vosk</div>
      <div class="watermark-divider"></div>
      <div class="watermark-tag">a creative agency</div>
    </div>
    <div class="contact">
      <div class="contact-row">
        <svg viewBox="0 0 16 16"><circle cx="8" cy="8" r="7" fill="var(--red)"/><path d="M4 5c2 0 3 1 2 3s1 3 0 5M10 3c-1 2 1 3 3 3" fill="none" stroke="#fff" stroke-width="1.2"/></svg>
        <span>http//www.voskstudio.com</span>
      </div>
      <div class="contact-row contact-row--social">
        <span>. @voskstudio</span>
      </div>
    </div>
  </section>

</main>
</body>
</html>
```